Business Card

We need a business card for a fundraising/sales and marketing company called Kelvora Appeals services. The logo colours are Red Black and white. The final design should communicate professional, reliable yet fun and charity minded
Updates

Sorry for the delay. A decision will be made in the next 48 hours. we are stuck between two designs. Kind Regards, Molly Ravenscroft

Industry/Entity Type

Marketing

```html
<!DOCTYPE html>
<html lang="en">
<head>
<meta charset="utf-8">
<title>Kelvora Appeals services – Business Card</title>
<link rel="stylesheet" href="https://fonts.googleapis.com/css2?family=Open+Sans:wght@400;600;700&display=swap">
<style>
  :root {
    --stage: #1b1b1b;
    --card: #ffffff;
    --ink: #1a1a1a;
    --ink-soft: #3a3a3a;
    --brand-red: #e0211f;
    --edge-dark: #4a4a4a;
  }
  * { box-sizing: border-box; margin: 0; padding: 0; }
  html, body {
    width: 1200px; height: 944px; overflow: hidden;
    background: var(--stage);
    font-family: "Open Sans", sans-serif;
  }
  .stage {
    position: relative; width: 1200px; height: 944px;
    display: flex; flex-direction: column; align-items: center; justify-content: center; gap: 60px;
  }
  .card {
    position: relative; width: 640px; height: 366px;
    background: var(--card); overflow: hidden;
  }
  .card__edge { position: absolute; left: 0; bottom: 0; width: 100%; height: 16px; }

  .brand-name {
    font-weight: 600; color: var(--brand-red); letter-spacing: .03em;
    white-space: nowrap; line-height: 1;
  }
  .brand-dot { flex: none; background: var(--brand-red); }

  /* Front */
  .front__mark {
    position: absolute; left: 50%; top: 150px; transform: translateX(-50%);
    display: flex; align-items: center; gap: 16px;
  }
  .front__mark .brand-dot { width: 22px; height: 22px; }
  .front__name { font-size: 42px; }

  /* Back */
  .back__person { position: absolute; left: 44px; top: 58px; }
  .back__name { font-size: 21px; font-weight: 700; color: var(--ink); line-height: 1.3; }
  .back__role { font-size: 13px; color: var(--brand-red); margin-left: 16px; }
  .contact {
    position: absolute; left: 44px; bottom: 40px; list-style: none;
    display: flex; flex-direction: column; gap: 6px;
  }
  .contact__item { display: flex; align-items: center; gap: 12px; font-size: 13px; color: var(--ink-soft); }
  .contact__icon { width: 14px; height: 14px; flex: none; }
  .back__mark {
    position: absolute; right: 26px; top: 36px; bottom: 50px;
    display: flex; flex-direction: column; align-items: center; justify-content: flex-end; gap: 12px;
  }
  .back__mark .brand-dot { width: 14px; height: 14px; }
  .back__name-vertical {
    writing-mode: vertical-rl; transform: rotate(180deg); font-size: 30px;
  }
</style>
</head>
<body>
<main class="stage">
  <section class="card card--front" aria-label="Card front">
    <div class="front__mark">
      <span class="brand-dot" aria-hidden="true"></span>
      <span class="brand-name front__name">Kelvora Appeals</span>
    </div>
    <svg class="card__edge" viewBox="0 0 640 16" preserveAspectRatio="none" aria-hidden="true">
      <rect x="0" y="11" width="640" height="5" fill="var(--edge-dark)"/>
      <polygon points="0,6 260,6 290,0 290,16 0,16" fill="var(--brand-red)"/>
    </svg>
  </section>

  <section class="card card--back" aria-label="Card back">
    <div class="back__person">
      <h1 class="back__name">Your Long Name</h1>
      <p class="back__role">Director</p>
    </div>
    <ul class="contact">
      <li class="contact__item">
        <svg class="contact__icon" viewBox="0 0 14 14" aria-hidden="true"><path d="M7 1a4 4 0 0 1 4 4c0 3-4 8-4 8S3 8 3 5a4 4 0 0 1 4-4z" fill="var(--brand-red)"/><circle cx="7" cy="5" r="1.5" fill="#fff"/></svg>
        Your current or commercial address
      </li>
      <li class="contact__item">
        <svg class="contact__icon" viewBox="0 0 14 14" aria-hidden="true"><path d="M2 4c0-1 1-2 2-2h6c1 0 2 1 2 2v1H9V4H5v1H2z M3 6h8l1 6H2z" fill="var(--brand-red)"/><circle cx="7" cy="9" r="1.6" fill="#fff"/></svg>
        00.00.00.0000
      </li>
      <li class="contact__item">
        <svg class="contact__icon" viewBox="0 0 14 14" aria-hidden="true"><rect x="1" y="3" width="12" height="8" fill="var(--brand-red)"/><path d="M1 3l6 5 6-5" fill="none" stroke="#fff" stroke-width="1"/></svg>
        yourname@yourwebsite.com
      </li>
      <li class="contact__item">
        <svg class="contact__icon" viewBox="0 0 14 14" aria-hidden="true"><circle cx="7" cy="7" r="6" fill="var(--brand-red)"/><path d="M1 7h12M7 1v12" stroke="#fff" stroke-width=".8" fill="none"/><ellipse cx="7" cy="7" rx="2.6" ry="6" stroke="#fff" stroke-width=".8" fill="none"/></svg>
        www.yourwebsite.com
      </li>
    </ul>
    <div class="back__mark">
      <span class="brand-dot" aria-hidden="true"></span>
      <span class="brand-name back__name-vertical">Kelvora Appeals</span>
    </div>
    <svg class="card__edge" viewBox="0 0 640 16" preserveAspectRatio="none" aria-hidden="true">
      <rect x="0" y="11" width="640" height="5" fill="var(--edge-dark)"/>
      <polygon points="0,6 320,6 350,0 350,16 0,16" fill="var(--brand-red)"/>
    </svg>
  </section>
</main>
</body>
</html>
```